The Get Me Hired as a Game Producer Business Card Design

I am currently looking for a business card to take along with me to the Play Makers Summit next year. It's my hope to get a business card that is memorable, fun and professional, and will encourage interest in myself and my abilities.

I'm Australian born and raised, and currently live here. I've studied for several years in Game Development and have managed projects professionally as a producer for around 2-3 years now. My job has been referred to as being a 'fire fighter' (hence the 'Game Dev Fire Dept' comment in the contact information). It's my job to prevent problems before they arise or to solve problems for team members as they happen.

I've got skills in time management, team management, project management, empathy, art and programming, as well as a great sense of humor. Whether or not this is something displayed on the card is your choice.

In past I've used a vector image of my face and colors in brown and blue, but this is not a theme I am particularly attached to if you can come up with something better and more creative.

Target Market(s)

Game Developers, Studio Leads, 25 years old and up

Industry/Entity Type

Business

Contact Information for Business Card

Velquaris,
Robert Kanlow,
robert@velquaris.com,
Game Producer/Developer (or Game Dev Fire Dept),

Requirements
Nice to have
• Consideration in the design for (or a second design for) a USB drive card.
http://www.plintrove.com.au/products/slim-usb-card

A space for my twitter account: @Velquaris

```html
<!DOCTYPE html>
<html lang="en">
<head>
<meta charset="utf-8">
<title>Velquaris – Robert Kanlow Business Card</title>
<link rel="stylesheet" href="https://fonts.googleapis.com/css2?family=Marcellus&family=Metamorphous&family=Orbitron:wght@600&family=Roboto+Condensed:wght@400&display=swap">
<style>
  :root {
    --page: #ffffff;
    --front-deep: #241010;
    --front-mid: #4a1c14;
    --front-band: rgba(190, 72, 40, .45);
    --front-band-soft: rgba(230, 110, 60, .22);
    --back-deep: #5e4446;
    --back-mid: #8c6a66;
    --back-band: rgba(240, 190, 170, .28);
    --back-band-soft: rgba(255, 220, 200, .16);
    --portrait-blue: #17557c;
    --portrait-blue-deep: #123f5e;
    --portrait-edge: #161616;
    --cream: #f4ecc6;
    --ink: #111111;
    --accent-red: #e3141b;
    --subtitle-blue: #7fb6e0;
    --subtitle-edge: #24466a;
    --contact: #ffffff;
  }
  * { margin: 0; padding: 0; box-sizing: border-box; }
  html, body { width: 1200px; height: 925px; overflow: hidden; background: var(--page); }
  .canvas { position: relative; width: 1200px; height: 925px; }

  .card { position: absolute; top: 0; height: 925px; overflow: hidden; }
  .band { position: absolute; width: 1400px; transform-origin: center; transform: rotate(-45deg); }

  /* Front */
  .card-front {
    left: 0; width: 575px;
    background: linear-gradient(155deg, var(--front-mid) 0%, var(--front-deep) 50%, var(--front-mid) 100%);
  }
  .card-front .band-a { left: -300px; top: 120px; height: 70px; background: var(--front-band); }
  .card-front .band-b { left: -260px; top: 230px; height: 26px; background: var(--front-band-soft); }
  .card-front .band-c { left: -420px; top: 520px; height: 110px; background: var(--front-band-soft); }
  .card-front .band-d { left: -480px; top: 690px; height: 40px; background: var(--front-band); }
  .card-front .band-e { left: -160px; top: 20px; height: 18px; background: var(--front-band-soft); }

  .portrait-front {
    position: absolute; left: 125px; top: 100px; width: 325px; height: 450px;
  }
  .brand-name {
    position: absolute; left: 0; width: 575px; top: 665px;
    text-align: center;
    font-family: "Marcellus", serif; font-weight: 400;
    font-size: 84px; line-height: 100px; color: var(--cream); letter-spacing: 1px;
  }
  .brand-reflection {
    position: absolute; left: 0; width: 575px; top: 742px;
    text-align: center;
    font-family: "Marcellus", serif; font-weight: 400;
    font-size: 84px; line-height: 100px; color: var(--cream); letter-spacing: 1px;
    transform: scaleY(-1); opacity: .22;
  }

  /* Back */
  .card-back {
    left: 630px; width: 570px;
    background: linear-gradient(165deg, var(--back-deep) 0%, var(--back-mid) 55%, var(--back-deep) 100%);
  }
  .card-back .band-a { left: -380px; top: 210px; height: 90px; background: var(--back-band); }
  .card-back .band-b { left: -300px; top: 120px; height: 24px; background: var(--back-band-soft); }
  .card-back .band-c { left: -450px; top: 430px; height: 60px; background: var(--back-band-soft); }
  .card-back .band-d { left: -520px; top: 600px; height: 120px; background: var(--back-band); }

  .portrait-faint {
    position: absolute; left: 10px; top: 150px; width: 370px; height: 380px;
  }
  .portrait-back {
    position: absolute; left: 332px; top: 333px; width: 260px; height: 590px;
  }
  .person-name {
    position: absolute; left: 40px; top: 40px; width: 495px; text-align: center;
    font-family: "Metamorphous", serif; font-weight: 400;
    font-size: 56px; line-height: 80px; color: var(--ink); white-space: nowrap;
    -webkit-text-stroke: 5px var(--accent-red); paint-order: stroke fill;
  }
  .name-rule {
    position: absolute; left: 57px; top: 140px; width: 455px; height: 9px;
    background: linear-gradient(90deg, var(--accent-red) 0 60%, var(--ink) 60% 100%);
  }
  .job-title {
    position: absolute; left: 30px; top: 160px; width: 510px; text-align: center;
    font-family: "Orbitron", sans-serif; font-weight: 600;
    font-size: 17px; line-height: 22px; color: var(--subtitle-blue);
    text-transform: uppercase; letter-spacing: 1.5px;
    -webkit-text-stroke: .6px var(--subtitle-edge);
  }
  .contact {
    position: absolute; left: 40px; top: 812px;
    font-family: "Roboto Condensed", sans-serif; font-weight: 400;
    font-size: 23px; line-height: 32px; color: var(--contact);
  }
</style>
</head>
<body>
<main class="canvas">
  <section class="card card-front">
    <div class="band band-a"></div>
    <div class="band band-b"></div>
    <div class="band band-c"></div>
    <div class="band band-d"></div>
    <div class="band band-e"></div>
    <svg class="portrait-front" viewBox="0 0 325 450" role="img" aria-label="Illustrated portrait of Robert Kanlow">
      <defs>
        <radialGradient id="front-fill" cx="50%" cy="45%" r="60%">
          <stop offset="0%" stop-color="var(--portrait-blue)"/>
          <stop offset="100%" stop-color="var(--portrait-blue-deep)"/>
        </radialGradient>
      </defs>
      <path d="M40 60 Q160 -10 290 50 Q330 160 300 300 Q250 440 160 445 Q70 440 30 300 Q-5 170 40 60 Z" fill="var(--portrait-edge)"/>
      <path d="M52 72 Q160 8 280 62 Q316 165 288 296 Q242 428 160 432 Q80 428 42 296 Q12 172 52 72 Z" fill="url(#front-fill)"/>
    </svg>
    <h1 class="brand-name">Velquaris</h1>
    <div class="brand-reflection" aria-hidden="true">Velquaris</div>
  </section>

  <section class="card card-back">
    <div class="band band-a"></div>
    <div class="band band-b"></div>
    <div class="band band-c"></div>
    <div class="band band-d"></div>
    <svg class="portrait-faint" viewBox="0 0 370 380" role="img" aria-label="Faint enlarged portrait in the background">
      <defs>
        <radialGradient id="faint-fill" cx="50%" cy="50%" r="50%">
          <stop offset="0%" stop-color="#3a2626" stop-opacity=".35"/>
          <stop offset="100%" stop-color="#3a2626" stop-opacity="0"/>
        </radialGradient>
      </defs>
      <ellipse cx="185" cy="190" rx="185" ry="190" fill="url(#faint-fill)"/>
    </svg>
    <svg class="portrait-back" viewBox="0 0 260 590" role="img" aria-label="Illustrated portrait of Robert Kanlow, partly cropped">
      <defs>
        <radialGradient id="back-fill" cx="60%" cy="45%" r="65%">
          <stop offset="0%" stop-color="var(--portrait-blue)"/>
          <stop offset="100%" stop-color="var(--portrait-blue-deep)"/>
        </radialGradient>
      </defs>
      <path d="M60 30 Q150 -10 260 10 L260 590 L200 590 Q80 560 30 380 Q-10 200 60 30 Z" fill="var(--portrait-edge)"/>
      <path d="M72 44 Q155 6 260 24 L260 576 L202 576 Q92 548 44 378 Q8 206 72 44 Z" fill="url(#back-fill)"/>
    </svg>
    <h2 class="person-name">Robert Kanlow.</h2>
    <div class="name-rule"></div>
    <p class="job-title">Game Producer / Developer<br>(or Game Dev Fire Dept),</p>
    <p class="contact">Phone : 91 400 555 018<br>Email : robert@velquaris.com,<br>Twitter : @Velquaris</p>
  </section>
</main>
</body>
</html>
```